New Business Card Design*

We are a recruitment company based in Hartmoor/Cambridge England.
I have included our company logo which we want to remain the same.

What we are looking for is a new creative Business card which will really stand out!!

Contact Information for Business Card

Harriet Vance
email: Harriet@brelvix.co.uk
Address: Tolworth House
Ashgrove Innovation Park
Pelham Road
Hartmoor
KT9 3QD
Tel:01632 960418

```html
<!DOCTYPE html>
<html lang="en">
<head>
<meta charset="utf-8">
<title>Brelvix Business Card</title>
<link rel="stylesheet" href="https://fonts.googleapis.com/css2?family=Lato:wght@400;700&display=swap">
<style>
  :root {
    --backdrop: #ecebe8;
    --card: #ffffff;
    --card-tint: #f8f8f8;
    --bar: #3e3e3e;
    --accent: #8cc63f;
    --ink-grey: #7b7b7b;
    --on-bar: #ffffff;
  }
  * { margin: 0; padding: 0; box-sizing: border-box; }
  html, body {
    width: 1200px;
    height: 801px;
    overflow: hidden;
    background: var(--backdrop);
    font-family: "Lato", sans-serif;
  }
  .canvas { position: relative; width: 1200px; height: 801px; }

  .card {
    position: absolute;
    background: var(--card);
    box-shadow: 0 3px 10px rgba(0,0,0,0.12);
    overflow: hidden;
  }
  .card--back { left: 310px; top: 250px; width: 248px; height: 448px; }
  .card--front { left: 604px; top: 138px; width: 251px; height: 449px; background: var(--card-tint); }

  .brand {
    position: absolute;
    display: flex;
    align-items: center;
    gap: 8px;
    left: 0; right: 0;
    justify-content: center;
  }
  .brand__dot {
    width: 28px; height: 28px;
    border-radius: 50%;
    background: var(--accent);
  }
  .brand__name {
    font-weight: 700;
    font-size: 30px;
    color: var(--ink-grey);
    letter-spacing: -0.3px;
  }
  .card--back .brand { top: 124px; }
  .card--front .brand { top: 124px; }

  .top-tab {
    position: absolute;
    left: 0; top: 0;
  }

  .contact-list { position: absolute; left: 0; right: 0; top: 252px; }
  .contact-row {
    display: flex;
    height: 41px;
    margin-bottom: 4px;
  }
  .contact-row--name { height: 42px; }
  .contact-row--address { height: 45px; }
  .contact-row__icon {
    width: 33px;
    background: var(--bar);
    display: flex; align-items: center; justify-content: center;
    margin-right: 2px;
  }
  .contact-row__icon svg { width: 17px; height: 17px; fill: var(--on-bar); }
  .contact-row__body {
    position: relative;
    flex: 1;
    background: var(--bar);
    color: var(--on-bar);
    display: flex; align-items: center;
    padding-left: 31px;
    font-size: 9.5px;
    line-height: 1.35;
    white-space: nowrap;
  }
  .contact-row__wedge {
    position: absolute; left: 0; top: 0;
    width: 24px; height: 100%;
  }
  .contact-row__wedge polygon { fill: var(--accent); }
  .contact-row--name .contact-row__body { font-size: 21px; }
  .contact-row--name strong { font-weight: 700; margin-left: 5px; }
</style>
</head>
<body>
<div class="canvas">

  <section class="card card--back">
    <div class="brand">
      <span class="brand__dot"></span>
      <span class="brand__name">Brelvix</span>
    </div>
  </section>

  <section class="card card--front">
    <svg class="top-tab" width="251" height="27" viewBox="0 0 251 27">
      <polygon points="29,0 206,0 196,27 40,27" fill="var(--accent)"/>
    </svg>

    <div class="brand">
      <span class="brand__dot"></span>
      <span class="brand__name">Brelvix</span>
    </div>

    <div class="contact-list">
      <div class="contact-row contact-row--name">
        <div class="contact-row__icon">
          <svg viewBox="0 0 20 20"><circle cx="10" cy="6" r="4.2"/><path d="M2 19c0-5 3.5-7.5 8-7.5s8 2.5 8 7.5z"/></svg>
        </div>
        <div class="contact-row__body">
          <svg class="contact-row__wedge" viewBox="0 0 24 42" preserveAspectRatio="none"><polygon points="0,0 24,0 0,42"/></svg>
          Harriet<strong>Vance</strong>
        </div>
      </div>

      <div class="contact-row contact-row--phone">
        <div class="contact-row__icon">
          <svg viewBox="0 0 20 20"><path d="M10 1a9 9 0 1 0 0 18a9 9 0 0 0 0-18zm0 1.6a7.4 7.4 0 1 1 0 14.8a7.4 7.4 0 0 1 0-14.8z"/><path d="M6.6 5.2l1.6-.4 1.2 2.6-1 .9c.5 1.3 1.5 2.4 2.8 3l.9-1 2.6 1.2-.4 1.6c-.2.6-.8 1-1.5.9-3.3-.6-5.9-3.2-6.6-6.4-.1-.7.2-1.3.4-1.4z"/></svg>
        </div>
        <div class="contact-row__body">
          <svg class="contact-row__wedge" viewBox="0 0 24 41" preserveAspectRatio="none"><polygon points="0,0 24,0 0,41"/></svg>
          01632 960418
        </div>
      </div>

      <div class="contact-row contact-row--web">
        <div class="contact-row__icon">
          <svg viewBox="0 0 20 20" fill="none"><g stroke="#fff" stroke-width="1.4" fill="none"><circle cx="10" cy="10" r="8"/><ellipse cx="10" cy="10" rx="3.5" ry="8"/><line x1="2" y1="10" x2="18" y2="10"/><path d="M3.5 5.5h13M3.5 14.5h13"/></g></svg>
        </div>
        <div class="contact-row__body">
          <svg class="contact-row__wedge" viewBox="0 0 24 41" preserveAspectRatio="none"><polygon points="0,0 24,0 0,41"/></svg>
          Harriet@brelvix.co.uk
        </div>
      </div>

      <div class="contact-row contact-row--address">
        <div class="contact-row__icon">
          <svg viewBox="0 0 20 20"><path d="M10 1a6 6 0 0 0-6 6c0 4.5 6 12 6 12s6-7.5 6-12a6 6 0 0 0-6-6zm0 8.3a2.3 2.3 0 1 1 0-4.6a2.3 2.3 0 0 1 0 4.6z"/></svg>
        </div>
        <div class="contact-row__body">
          <svg class="contact-row__wedge" viewBox="0 0 24 45" preserveAspectRatio="none"><polygon points="0,0 24,0 0,45"/></svg>
          <span>Tolworth House, Ashgrove Innovation Park<br>Pelham Road, Hartmoor, KT9 3QD</span>
        </div>
      </div>
    </div>
  </section>

</div>
</body>
</html>
```